Driftwood Dales Restaurant Web Design

Driftwood Dales Grill and Bar

https://driftwooddales.example
Logo available on existing website.

Images Availble at Social Media
www.facebook.com/driftwooddales/
www.instagram.com/driftwooddales/

Driftwood Dales is a full service Restaurant and bar on Pelican Shoal Key, FL. They are highlited by excellent food in a casual Island sports atmosphere. They are frequented by Locals and Tourist Alike. We would like to push the quality of their food which includes a large menu variety, a late night full liqour bar with sports and TVs, and a convenient location at the front of the Island. They have very good reviews from google and FB.

1. Header and Footer Template
A. Header Template
1. Logo
2. Social Icons | Phone # and Icon | Address | Reviews Icon
3. Main Menu - With Dropdowns
a.Menus - Dinner, Lunch, Drinks - Liqour, Wine, Beer, Specials
b.About us - About us, Local Links, Disclaimer, Privacy policy, Accessability
c.Blog/ Calendar/Events
d. Contact Us
B. Footer Template -
1. Static Banner with Logo links to DD Liqour, 7128, mvt liqour
1. Duplicate Above Info - Different Layout
2. Socket with Copyright etc.

2. Front Page
A. Hero Section - Image Slider? h1 Tag + Description
B. Food Menu Images and Links Section
C. Daily Specials Post (single Post Layout - MENU CPT - Daily Special Category)
D. Testimonials Slider -Include link to more reviews (google, Trip Advisor etc.)
E. Blog / Events 3 column Post Section.
A static Banner Ad needs to be at the bottom linking to Driftwood Spirits and Coffee shop

3. Inernal Pages
A. Blog Template Page for Events/Blog - If we go with a calendar plugin this will deviate.

B. Menu CPT - food-menu - set your slug / rewrite url: restaurant-pelican-shoal-key
1. Each Menu will need a page template to display menu items. Lunch/Dinner/Specials/Drinks (liqour,Beer,Wine )

C. Contact Us Page - No Form - Google Map - Location address phone.
D. About Us Page - Static Page - Images and content to Highlight Quality of Food. Late Night Bar - Sports Bar

E. Static Pages - Accessabily Page, Privacy Policy, DisclaimerRestaurant Website Redesign.

Industry/Entity Type

Restaraunt

Number of Pages Required

5+ page

Requirements
Nice to have
• Please give us some unique restaurant designs. not a standard template

```html
<!DOCTYPE html>
<html lang="en">
<head>
<meta charset="utf-8">
<title>Driftwood Dales Grill and Bar</title>
<link href="https://fonts.googleapis.com/css2?family=Oswald:wght@300;400;500;700&family=Lato:wght@400;700&display=swap" rel="stylesheet">
<style>
:root{
  --orange:#ff7f00;
  --ink:#111111;
  --bar:#1a1a1a;
  --soft:#f2f2f2;
  --white:#ffffff;
  --text:#222222;
  --muted:#888888;
}
*{box-sizing:border-box;margin:0;padding:0}
html,body{width:1200px;height:4254px;overflow:hidden}
body{position:relative;background:var(--white);font-family:'Oswald',sans-serif;color:var(--text)}
.abs{position:absolute}
a{color:inherit;text-decoration:none}

/* top bar */
.topbar{left:0;top:0;width:1200px;height:58px;background:var(--bar);font-family:'Lato',sans-serif;color:#fff;font-size:14px}
.social{top:15px;width:28px;height:28px;border-radius:50%;background:var(--orange)}
.icon-circle{width:32px;height:32px;border-radius:50%;background:var(--orange);display:flex;align-items:center;justify-content:center}
.topbar .contact{display:flex;align-items:center;gap:10px;line-height:1.2}
.review-box{left:1063px;top:12px;width:36px;height:36px;border:2px solid var(--orange);border-radius:6px}

/* nav */
.nav{left:0;top:58px;width:1200px;height:66px;background:#fff;border-bottom:1px solid #eee}
.brand{left:100px;top:68px;font-size:32px;letter-spacing:4px;font-weight:500;color:#111;line-height:44px}
.menu{top:78px;font-size:16px;color:#222;display:flex;align-items:center;gap:5px;font-family:'Lato',sans-serif}
.caret{width:0;height:0;border-left:5px solid transparent;border-right:5px solid transparent;border-top:6px solid var(--orange)}

/* hero */
.hero{left:0;top:124px;width:1200px;height:605px;background:linear-gradient(180deg,#2f72c6 0%,#6ea6e0 35%,#b9d6ec 50%,#3d9fb2 58%,#e6e0d2 68%,#d8cfbd 82%,#8a6a48 100%)}
.hero-text{left:0;width:1200px;text-align:center;color:#fff}
.btn{display:flex;align-items:center;justify-content:center;gap:14px;background:var(--orange);color:#fff;font-size:21px;border-radius:4px}
.btn .dot{width:22px;height:22px;border-radius:50%;background:#fff;display:flex;align-items:center;justify-content:center}

/* section titles */
.sec-title{color:var(--orange);font-size:42px;font-weight:400;text-align:center;line-height:1}
.bracket{position:relative;display:inline-block;padding:6px 12px}
.bracket::before,.bracket::after{content:"";position:absolute;top:18px;bottom:0;width:14px;border-bottom:3px solid var(--orange)}
.bracket::before{left:0;border-left:3px solid var(--orange)}
.bracket::after{right:0;border-right:3px solid var(--orange)}
.bracket.tl::before,.bracket.tl::after{top:14px;bottom:4px;border-bottom:none;border-top:3px solid var(--orange)}

/* about */
.about-frame{left:30px;top:848px;width:477px;height:464px;border:5px solid var(--orange)}
.about-photo{left:52px;top:814px;width:478px;height:476px;background:radial-gradient(ellipse at 50% 40%,#2a3060 0%,#12142e 45%,#0a0b1c 70%),linear-gradient(180deg,#0a0c22,#5a3a22)}
.about-copy{left:601px;top:920px;width:460px;font-size:30px;font-weight:300;color:var(--muted);line-height:41px}
.bottles{left:1000px;top:980px;width:200px;height:335px;background:linear-gradient(90deg,rgba(255,255,255,0) 0%,#e6ece9 40%,#d2ddd7 100%)}

/* menus */
.menus{left:0;top:1416px;width:1200px;height:644px;background:var(--soft)}
.tab{top:1555px;font-size:34px;font-weight:300;color:#222}
.tab-line{top:1620px;height:2px}
.card{top:1657px;width:239px;height:310px;border-radius:4px;overflow:hidden}
.card-label{position:absolute;left:0;bottom:24px;width:100%;text-align:center;color:#fff;font-size:40px;font-weight:400}

/* daily special */
.special{left:0;top:2062px;width:1200px;height:648px;background:linear-gradient(90deg,#0d0d0d 0%,#121110 45%,#3a2814 58%,#a06a2c 72%,#c99a52 85%,#7a4e1e 100%)}
.special-copy{left:97px;color:#fff}

/* testimonials */
.testi{left:208px;top:2880px;width:787px;height:282px;background:#fff;border-radius:0 0 90px 0;box-shadow:4px 10px 22px rgba(0,0,0,.12)}
.testi-text{left:280px;top:2925px;width:650px;text-align:center;font-size:17px;line-height:27px;color:#222;font-weight:300}
.badge{top:3092px;height:40px;border-radius:20px}

/* blog */
.post{top:3358px;width:309px;height:382px;background:#fff;box-shadow:0 4px 14px rgba(0,0,0,.12);border-radius:6px;overflow:hidden}
.post-img{width:100%;height:177px}
.pill{position:absolute;top:14px;right:10px;background:var(--orange);color:#fff;font-size:10px;padding:6px 14px;border-radius:12px;font-family:'Lato',sans-serif}
.post-text{text-align:center;font-size:22px;line-height:37px;color:#222;font-weight:400;padding-top:18px}
.post .btn{position:absolute;left:74px;bottom:18px;width:162px;height:42px}

/* footer */
.footer{left:0;top:3806px;width:1200px;height:370px;background:var(--ink);color:#fff}
.foot-head{top:3890px;font-size:21px;font-weight:500;letter-spacing:.5px;color:#fff}
.foot-list{top:3945px;font-size:14px;line-height:30px;color:#fff;font-weight:400;list-style:none}
.foot-contact{font-size:14px;line-height:21px;color:#fff}
.ring{width:28px;height:28px;border-radius:50%;border:2px solid var(--orange);display:flex;align-items:center;justify-content:center;flex:none}
.foot-photo{left:782px;top:3950px;width:321px;height:145px;background:linear-gradient(90deg,#3a2a20 0%,#6b5040 45%,#a7c7a0 70%,#4aa85a 100%)}
.socket{left:0;top:4176px;width:1200px;height:78px;background:var(--orange);color:#fff;font-size:16px;text-align:center;line-height:78px}
</style>
</head>
<body>

<header class="abs topbar">
  <span class="abs social" style="left:98px"></span>
  <span class="abs social" style="left:138px"></span>
  <span class="abs social" style="left:177px"></span>
  <div class="abs contact" style="left:510px;top:13px">
    <span class="icon-circle"><svg width="16" height="16" viewBox="0 0 24 24"><path fill="#fff" d="M6.6 10.8a15 15 0 0 0 6.6 6.6l2.2-2.2c.3-.3.7-.4 1-.2 1.1.4 2.3.6 3.6.6.6 0 1 .4 1 1V20c0 .6-.4 1-1 1A17 17 0 0 1 3 4c0-.6.4-1 1-1h3.5c.6 0 1 .4 1 1 0 1.3.2 2.5.6 3.6.1.3 0 .7-.2 1z"/></svg></span>
    <span>+1 941-555-0142</span>
  </div>
  <div class="abs contact" style="left:755px;top:10px">
    <span class="icon-circle"><svg width="14" height="18" viewBox="0 0 24 30"><path fill="#fff" d="M12 0C5.4 0 0 5.3 0 12c0 9 12 18 12 18s12-9 12-18C24 5.3 18.6 0 12 0zm0 17a5 5 0 1 1 0-10 5 5 0 0 1 0 10z"/></svg></span>
    <span style="font-size:13px">1820 Shoreline Dr, Pelican Shoal Key,<br>FL 34990</span>
  </div>
  <span class="abs review-box"></span>
</header>

<nav class="abs nav"></nav>
<a class="abs brand" href="https://driftwooddales.example">DRIFTWOOD DALES</a>
<span class="abs menu" style="left:509px">Home</span>
<span class="abs menu" style="left:594px">About Us <i class="caret"></i></span>
<span class="abs menu" style="left:713px">Menu <i class="caret"></i></span>
<span class="abs menu" style="left:810px">Blog</span>
<span class="abs menu" style="left:882px">Contact Us</span>
<svg class="abs" style="left:1038px;top:80px" width="16" height="16" viewBox="0 0 24 24"><path fill="none" stroke="#ff7f00" stroke-width="2.5" d="M1 2h4l3 12h12l3-9H7"/><circle cx="9" cy="20" r="2" fill="#ff7f00"/><circle cx="18" cy="20" r="2" fill="#ff7f00"/></svg>
<svg class="abs" style="left:1086px;top:80px" width="16" height="16" viewBox="0 0 24 24"><circle cx="10" cy="10" r="7" fill="none" stroke="#ff7f00" stroke-width="3"/><path d="M15 15l7 7" stroke="#ff7f00" stroke-width="3"/></svg>

<section class="abs hero" role="img" aria-label="Beach boardwalk between palm trees leading to the sea under a blue sky"></section>
<p class="abs hero-text" style="top:280px;font-size:28px;font-weight:400">WELCOME TO</p>
<h1 class="abs hero-text" style="top:310px;font-size:80px;font-weight:700;letter-spacing:1px;line-height:1.1">DRIFTWOOD DALES</h1>
<p class="abs hero-text" style="top:400px;font-size:22px;font-weight:400">Great food ,Cocktails,Craft Beer</p>
<a class="abs btn" style="left:528px;top:443px;width:144px;height:40px" href="#">Book Now <span class="dot"><svg width="12" height="12" viewBox="0 0 12 12"><path d="M2 6h7M6 3l3 3-3 3" stroke="#ff7f00" stroke-width="2" fill="none"/></svg></span></a>

<div class="abs about-frame"></div>
<div class="abs about-photo" role="img" aria-label="Restaurant front lit with neon signs at night"></div>
<h2 class="abs sec-title" style="left:601px;top:846px"><span class="bracket tl">About US</span></h2>
<p class="abs about-copy">Casual atmosphere restaurant serving lunch and dinner. Full bar that is open late. Come check us out and see why we are the Island Locals' favorite spot!</p>
<a class="abs btn" style="left:606px;top:1112px;width:162px;height:45px" href="#">Read More <span class="dot"><svg width="12" height="12" viewBox="0 0 12 12"><path d="M2 6h7M6 3l3 3-3 3" stroke="#ff7f00" stroke-width="2" fill="none"/></svg></span></a>
<div class="abs bottles" role="img" aria-label="Two bottles of white rum"></div>

<section class="abs menus"></section>
<h2 class="abs sec-title" style="left:0;width:1200px;top:1463px"><span class="bracket tl">Our Menus</span></h2>
<span class="abs tab" style="left:418px">Dinner</span>
<span class="abs tab" style="left:565px">Lunch</span>
<span class="abs tab" style="left:703px">Drinks</span>
<span class="abs tab-line" style="left:418px;width:364px;background:#ddd"></span>
<span class="abs tab-line" style="left:700px;width:82px;background:var(--orange);top:1619px;height:3px"></span>

<div class="abs card" style="left:97px;background:linear-gradient(180deg,#2a2a2a,#5a5a4a 60%,#3a3a30)" role="img" aria-label="Liquor bottles on a shelf"><span class="card-label">Liqour</span></div>
<div class="abs card" style="left:354px;background:linear-gradient(180deg,#2a2a2a,#6a5a2a 55%,#3a2a20)" role="img" aria-label="Wine bottles in a row"><span class="card-label">Wine</span></div>
<div class="abs card" style="left:609px;background:linear-gradient(180deg,#4a3020,#8a5a30 55%,#3a2010)" role="img" aria-label="Wooden barrel"><span class="card-label">Beer</span></div>
<div class="abs card" style="left:866px;background:linear-gradient(135deg,#c9c2b2,#6a3a2a 45%,#8a6a4a 75%,#d8d2c5)" role="img" aria-label="Plated steak with vegetables"><span class="card-label">Specials</span></div>

<section class="abs special" role="img" aria-label="Crispy fried wontons drizzled with sauce over greens"></section>
<div class="abs special-copy" style="top:2205px">
  <h2 style="font-size:74px;font-weight:700;line-height:1">Daily Special</h2>
  <h3 style="font-size:58px;font-weight:500;line-height:1;margin-top:28px">Dinner</h3>
  <p style="font-size:14px;font-weight:300;line-height:26px;width:560px;margin-top:22px">Sed ut perspiciatis unde omnis iste natus error sit voluptatem accusantium doloremque laudantium, totam rem aperiam, eaque ipsa quae ab illo inventore veritatis et quasi architecto beatae vitae dicta sunt explicabo. Nemo enim ipsam voluptatem quia voluptas</p>
</div>
<a class="abs btn" style="left:93px;top:2508px;width:162px;height:42px" href="#">Our Menu <span class="dot"><svg width="12" height="12" viewBox="0 0 12 12"><path d="M2 6h7M6 3l3 3-3 3" stroke="#ff7f00" stroke-width="2" fill="none"/></svg></span></a>

<h2 class="abs sec-title" style="left:0;width:1200px;top:2815px;color:#111"><span class="bracket">Testimonials</span></h2>
<div class="abs testi"></div>
<p class="abs testi-text">Lorem ipsum dolor sit amet, consectetur adipiscing elit, sed do eiusmod tempor incididunt ut labore et dolore magna aliqua. Ut enim ad minim veniam, quis nostrud exercitation ullamco laboris nisi ut aliquip ex ea commodo consequat.Lorem ipsum dolor sit amet, consectetur adipiscing elit, sed do eiusmod tempor incididunt ut labore et dolore magna aliqua. Ut enim ad minim veniam, quis nostrud exercitation ullamco</p>
<svg class="abs" style="left:236px;top:3002px" width="14" height="20" viewBox="0 0 14 20"><path d="M11 2L3 10l8 8" stroke="#aaa" stroke-width="3" fill="none"/></svg>
<svg class="abs" style="left:953px;top:2996px" width="14" height="20" viewBox="0 0 14 20"><path d="M3 2l8 8-8 8" stroke="#111" stroke-width="3" fill="none"/></svg>
<span class="abs badge" style="left:417px;width:120px;background:#e9eef7" role="img" aria-label="Review site badge"></span>
<span class="abs badge" style="left:582px;width:200px;background:#e6f3ee" role="img" aria-label="Travel review site badge"></span>

<h2 class="abs sec-title" style="left:0;width:1200px;top:3268px;color:#111"><span class="bracket">Our Blog</span></h2>

<article class="abs post" style="left:99px">
  <div class="post-img" style="background:linear-gradient(180deg,#9ab4c8,#7a8a92 55%,#c8c0b0)" role="img" aria-label="Costumed holiday figure walking reindeer along the beach"></div>
  <span class="pill">DEC 27, 2022</span>
  <p class="post-text">Lorem ipsum dolor sit amet,<br>consectetur adipiscing elit,<br>sed do eiusmod</p>
  <a class="btn" href="#">Read More <span class="dot"><svg width="12" height="12" viewBox="0 0 12 12"><path d="M2 6h7M6 3l3 3-3 3" stroke="#ff7f00" stroke-width="2" fill="none"/></svg></span></a>
</article>
<article class="abs post" style="left:446px">
  <div class="post-img" style="background:linear-gradient(180deg,#6aa0d0,#3a8a3a 50%,#a02020)" role="img" aria-label="Guests in green festival costumes beside a red vehicle"></div>
  <span class="pill">DEC 27, 2022</span>
  <p class="post-text">Lorem ipsum dolor sit amet,<br>consectetur adipiscing elit,<br>sed do eiusmod</p>
  <a class="btn" href="#">Read More <span class="dot"><svg width="12" height="12" viewBox="0 0 12 12"><path d="M2 6h7M6 3l3 3-3 3" stroke="#ff7f00" stroke-width="2" fill="none"/></svg></span></a>
</article>
<article class="abs post" style="left:792px">
  <div class="post-img" style="background:linear-gradient(180deg,#c8d4da,#5a8a5a 55%,#2a4a2a)" role="img" aria-label="Bartender in a green shirt behind the bar"></div>
  <span class="pill">DEC 27, 2022</span>
  <p class="post-text">Lorem ipsum dolor sit amet,<br>consectetur adipiscing elit,<br>sed do eiusmod</p>
  <a class="btn" href="#">Read More <span class="dot"><svg width="12" height="12" viewBox="0 0 12 12"><path d="M2 6h7M6 3l3 3-3 3" stroke="#ff7f00" stroke-width="2" fill="none"/></svg></span></a>
</article>

<footer class="abs footer"></footer>
<h4 class="abs foot-head" style="left:98px">QUICK LINK</h4>
<ul class="abs foot-list" style="left:103px"><li>Home</li><li>About Us</li><li>Menu</li><li>Blog</li><li>Contact Us</li></ul>
<h4 class="abs foot-head" style="left:308px">OUR MENU</h4>
<ul class="abs foot-list" style="left:312px;line-height:23px"><li>Dinner</li><li>Lunch</li><li>Drinks - Liqour</li><li>Wine</li><li>Beer</li><li>Specials</li></ul>
<h4 class="abs foot-head" style="left:517px">GET IN TOUCH</h4>
<div class="abs foot-contact" style="left:517px;top:3936px;display:flex;gap:14px"><span class="ring"><svg width="10" height="13" viewBox="0 0 24 30"><path fill="#ff7f00" d="M12 0C5.4 0 0 5.3 0 12c0 9 12 18 12 18s12-9 12-18C24 5.3 18.6 0 12 0zm0 17a5 5 0 1 1 0-10 5 5 0 0 1 0 10z"/></svg></span><span>1820 Shoreline Dr,<br>Pelican Shoal Key, FL 34990</span></div>
<div class="abs foot-contact" style="left:517px;top:4003px;display:flex;gap:14px;align-items:center"><span class="ring"><svg width="12" height="12" viewBox="0 0 24 24"><path fill="#ff7f00" d="M6.6 10.8a15 15 0 0 0 6.6 6.6l2.2-2.2c.3-.3.7-.4 1-.2 1.1.4 2.3.6 3.6.6.6 0 1 .4 1 1V20c0 .6-.4 1-1 1A17 17 0 0 1 3 4c0-.6.4-1 1-1h3.5c.6 0 1 .4 1 1 0 1.3.2 2.5.6 3.6.1.3 0 .7-.2 1z"/></svg></span><span>+1 941-555-0142</span></div>
<div class="abs foot-contact" style="left:517px;top:4060px;display:flex;gap:14px;align-items:center"><span class="ring"><svg width="12" height="10" viewBox="0 0 24 18"><rect x="1" y="1" width="22" height="16" fill="none" stroke="#ff7f00" stroke-width="2"/><path d="M1 1l11 9 11-9" fill="none" stroke="#ff7f00" stroke-width="2"/></svg></span><span>info@driftwooddales.example</span></div>
<a class="abs" style="left:780px;top:3888px;font-size:26px;letter-spacing:3px;font-weight:500;color:#fff" href="https://driftwooddales.example">DRIFTWOOD DALES</a>
<div class="abs foot-photo" role="img" aria-label="Bar interior with partner shop signs and a cocktail"></div>

<div class="abs socket">Copyright © 2023 Driftwood Dales Grill and Bar. All Rights Reserved</div>

</body>
</html>
```